Harrowgate Supply Group Business Card Design

The Business Card will be one side only with Harrowgate Supplies Group Logo
Card should have:
Name
Title
Office phone Number
Cell Number
email address
Website
Street Address
Our Slogan is Rugged and Reliable
Looking for something that stands out from other business cards

Target Market(s)

Heavy equipment Lease Company

```html
<!DOCTYPE html>
<html lang="en">
<head>
<meta charset="utf-8">
<title>Harrowgate Supplies Group – Business Card</title>
<link rel="stylesheet" href="https://fonts.googleapis.com/css2?family=Arimo:wght@400;700&family=Open+Sans:wght@400&display=swap">
<style>
  :root{
    --red:#e31a38;
    --navy:#272a72;
    --white:#ffffff;
    --silver-dark:#9a9ca1;
    --silver-light:#f2f2f3;
    --backdrop-a:#e2e3e4;
    --backdrop-b:#c8c9cb;
    --edge:#a9abaf;
  }
  *{margin:0;padding:0;box-sizing:border-box}
  html,body{width:1200px;height:1158px;overflow:hidden}
  body{
    position:relative;
    background:linear-gradient(90deg,var(--backdrop-a),var(--backdrop-b));
    font-family:"Arimo",Arial,sans-serif;
  }
  .card{position:absolute;width:749px;height:428px;overflow:hidden}
  .card-front{left:363px;top:110px;border-radius:12px;border:1px solid var(--edge);background:var(--white)}
  .card-back{left:87px;top:617px;border-radius:40px;background:var(--red)}
  .front-waves{position:absolute;inset:0;width:100%;height:100%}

  .brand{
    position:absolute;right:38px;top:70px;
    display:flex;align-items:center;gap:12px;
    font-family:"Arimo",Arial,sans-serif;font-weight:700;font-size:22px;
    color:var(--red);letter-spacing:.2px;
  }
  .brand-dot{width:26px;height:26px;border-radius:50%;background:var(--navy)}

  .holder{position:absolute;left:30px;top:254px;color:var(--white)}
  .holder-name{font-weight:700;font-size:24px;letter-spacing:.3px}
  .holder-title{font-size:19px;margin-top:6px;letter-spacing:.4px}
  .holder-address{font-family:"Open Sans",Arial,sans-serif;font-size:17.5px;line-height:26px;margin-top:22px}

  .contacts{position:absolute;right:18px;top:281px;list-style:none;color:var(--white);
    font-family:"Open Sans",Arial,sans-serif;font-size:18px}
  .contacts li{display:flex;align-items:center;justify-content:flex-end;gap:12px;height:34px;letter-spacing:.3px}
  .contacts svg{width:20px;height:20px;flex:none}

  .back-name{
    position:absolute;left:0;right:0;top:175px;text-align:center;
    font-weight:700;font-size:36px;color:var(--white);letter-spacing:.5px;
  }
  .slogan{
    position:absolute;left:0;right:0;top:388px;
    display:flex;align-items:center;justify-content:center;gap:14px;
    color:var(--white);font-weight:700;font-size:20px;letter-spacing:.3px;
  }
  .slogan-rule{width:88px;height:2px}
  .slogan-rule.left{background:linear-gradient(90deg,transparent,rgba(255,255,255,.75))}
  .slogan-rule.right{background:linear-gradient(90deg,rgba(255,255,255,.75),transparent)}
</style>
</head>
<body>

<section class="card card-front" aria-label="Business card front">
  <svg class="front-waves" viewBox="0 0 773 442" preserveAspectRatio="none" aria-hidden="true">
    <defs>
      <linearGradient id="silverSweep" x1="0" y1="0" x2="1" y2="0">
        <stop offset="0" stop-color="var(--silver-dark)"/>
        <stop offset="0.7" stop-color="var(--silver-light)"/>
        <stop offset="1" stop-color="var(--silver-dark)"/>
      </linearGradient>
      <linearGradient id="silverRise" x1="0" y1="1" x2="1" y2="0">
        <stop offset="0" stop-color="var(--silver-dark)"/>
        <stop offset="0.5" stop-color="var(--silver-light)"/>
        <stop offset="1" stop-color="var(--silver-dark)"/>
      </linearGradient>
    </defs>
    <path d="M0,132 C250,200 520,240 773,212 L773,442 L0,442 Z" fill="url(#silverSweep)"/>
    <path d="M0,160 C250,226 520,246 773,212 L773,442 L0,442 Z" fill="var(--red)"/>
    <path d="M0,0 H22 C170,120 430,222 773,212 C520,240 250,200 0,132 Z" fill="var(--navy)"/>
    <path d="M773,212 C520,262 300,360 182,442 L773,442 Z" fill="url(#silverRise)"/>
    <path d="M773,212 C560,272 380,362 262,442 L773,442 Z" fill="var(--navy)"/>
  </svg>

  <div class="brand"><span class="brand-dot"></span><span class="brand-name">HARROWGATE SUPPLIES GROUP</span></div>

  <div class="holder">
    <p class="holder-name">DANA WHITFIELD</p>
    <p class="holder-title">PRESIDENT</p>
    <p class="holder-address">Street Name, City Name<br>Zipcode - 01234</p>
  </div>

  <ul class="contacts">
    <li>012-345-6789
      <svg viewBox="0 0 20 20" aria-label="Office phone"><path d="M4 2 L7.5 2 L8.5 6 L6.5 7.5 C7.5 10 9.5 12 12 13.2 L13.5 11.3 L17.5 12.3 L17.5 15.8 C17.5 17 16.5 18 15 17.8 C8.5 17 3 11.5 2.2 5 C2 3.5 3 2 4 2 Z" fill="var(--white)"/></svg>
    </li>
    <li>012-345-6789
      <svg viewBox="0 0 20 20" aria-label="Cell phone"><circle cx="10" cy="10" r="8.6" fill="none" stroke="var(--white)" stroke-width="1.5"/><rect x="7" y="5" width="6" height="10" rx="1" fill="none" stroke="var(--white)" stroke-width="1.4"/><circle cx="10" cy="13" r=".8" fill="var(--white)"/></svg>
    </li>
    <li>office@harrowgatesupplies.com
      <svg viewBox="0 0 20 20" aria-label="Email"><rect x="1.5" y="4" width="17" height="12" fill="var(--white)"/><path d="M1.5 4 L10 11 L18.5 4 M1.5 16 L7.5 9.5 M18.5 16 L12.5 9.5" fill="none" stroke="var(--navy)" stroke-width="1.3"/></svg>
    </li>
    <li>www.harrowgatesupplies.com
      <svg viewBox="0 0 20 20" aria-label="Website"><g fill="none" stroke="var(--white)" stroke-width="1.4"><circle cx="10" cy="10" r="8.3"/><ellipse cx="10" cy="10" rx="3.8" ry="8.3"/><path d="M1.7 10 H18.3 M3 5.5 H17 M3 14.5 H17"/></g></svg>
    </li>
  </ul>
</section>

<section class="card card-back" aria-label="Business card back">
  <p class="back-name">HARROWGATE SUPPLIES GROUP</p>
  <p class="slogan"><span class="slogan-rule left"></span>RUGGED AND RELIABLE<span class="slogan-rule right"></span></p>
</section>

</body>
</html>
```